Welvira.io amazing image design

This is *not* a logo! We need a typography design for the phrase "what makes you, you?" to capture people's attention when a user posts their psychological test results to QN.
We need the design to stand out and color to make it grab attention. Font should not be anything like Comic Sans! Think Lorcan Vettridge!!!
Image needs to be sized and optimized for typical QN post (1200x630).

check us out at welvira.io

Target Market(s)

social media. as in, everyone who wants to learn more about themselves

Industry/Entity Type

Management Consulting

Logo Text

what makes you, you?

Colors

Designer to choose colors to be used in the design.

Requirements
Must have
• impact, originality, irony.
Nice to have
• an arresting image or colors
Should not have
• comic sans. dullness. sameness.

```html
<!DOCTYPE html>
<html lang="en">
<head>
<meta charset="utf-8">
<title>What makes you, you?</title>
<link rel="stylesheet" href="https://fonts.googleapis.com/css2?family=Jost:wght@500;600&family=Permanent+Marker&display=swap">
<style>
  :root {
    --page: #ffffff;
    --navy: #1d1a6e;
    --indigo: #2a2a9a;
    --cyan: #2fb3c4;
    --teal: #1f8f8a;
    --lime: #d6e63a;
    --ember: #b8352a;
    --ink: #0c0c14;
    --silver: rgba(214, 214, 214, 0.86);
    --silver-script: rgba(226, 226, 226, 0.9);
  }
  html, body {
    margin: 0;
    padding: 0;
    width: 1200px;
    height: 1000px;
    overflow: hidden;
    background: var(--page);
  }
  .poster {
    position: relative;
    width: 1200px;
    height: 1000px;
    background: var(--page);
  }
  .portrait-field {
    position: absolute;
    left: 177px;
    top: 0;
    width: 850px;
    height: 1000px;
    background:
      radial-gradient(ellipse 180px 260px at 50% 40%, var(--lime) 0%, rgba(214,230,58,0) 100%),
      radial-gradient(ellipse 160px 90px at 27% 40%, rgba(12,12,20,0.85) 0%, rgba(12,12,20,0) 100%),
      radial-gradient(ellipse 160px 90px at 73% 40%, rgba(12,12,20,0.85) 0%, rgba(12,12,20,0) 100%),
      radial-gradient(ellipse 120px 160px at 12% 45%, rgba(184,53,42,0.75) 0%, rgba(184,53,42,0) 100%),
      radial-gradient(ellipse 120px 160px at 88% 45%, rgba(184,53,42,0.75) 0%, rgba(184,53,42,0) 100%),
      radial-gradient(ellipse 140px 70px at 50% 82%, rgba(12,12,20,0.8) 0%, rgba(12,12,20,0) 100%),
      radial-gradient(ellipse 420px 560px at 50% 50%, var(--cyan) 0%, var(--teal) 45%, var(--indigo) 75%, var(--navy) 100%);
  }
  .headline {
    position: absolute;
    left: 0;
    top: 0;
    width: 1200px;
    height: 1000px;
  }
  .headline__line {
    font-family: "Jost", "Futura", sans-serif;
    font-weight: 500;
    fill: var(--silver);
  }
  .headline__script {
    font-family: "Permanent Marker", "Brush Script MT", cursive;
    fill: var(--silver-script);
  }
</style>
</head>
<body>
<main class="poster">
  <div class="portrait-field" role="img" aria-label="Close-up portrait of a face painted in vivid blue, cyan, lime and red powder pigments"></div>
  <svg class="headline" viewBox="0 0 1200 1000" aria-label="What makes you, you?">
    <text class="headline__line" x="265" y="232" font-size="290" textLength="708" lengthAdjust="spacingAndGlyphs">WHAT</text>
    <text class="headline__line" x="192" y="528" font-size="320" textLength="810" lengthAdjust="spacingAndGlyphs">MAKES</text>
    <text class="headline__line" x="298" y="730" font-size="290" textLength="612" lengthAdjust="spacingAndGlyphs">YOU,</text>
    <text class="headline__script" x="392" y="892" font-size="150" textLength="330" lengthAdjust="spacingAndGlyphs" transform="rotate(-4 557 840)">YOU?</text>
  </svg>
</main>
</body>
</html>
```